Dunwick Consulting Powerpoint Template

I require a powerpoint template that I can use for presentations and for report writing. Template should include:
* Cover page with company logo and space for presentation title, and client logo if required.
* Proposed font and heading styles to match the logo (demonstrated through some sample text)
* Three different examples of presentation pages that can be tailored to different clients
* End page for contact details of the presenter or other report details. (so template should be five pages in total length)

The overall style of the template is professional, but with an eye-catching style.

Target Market(s)

Government clients

Industry/Entity Type

Government

Requirements
Must have
• Three different presentation pages that can be optional.
• Proposed font / heading styles for presentation with sample texts
• Use colour pallet: http://www.huetrellis.net/palette/417096/Velvet_Harbor
• Clear, crisp and professional design.
Should not have
• Pictures

```html
<!DOCTYPE html>
<html lang="en">
<head>
<meta charset="utf-8">
<title>Dunwick Consulting – Title Page Notes</title>
<link rel="stylesheet" href="https://fonts.googleapis.com/css2?family=Questrial&display=swap">
<style>
  :root {
    --navy: #04375e;
    --sage: #9fb3b1;
    --sand: #d9c0a7;
    --slate: #787878;
    --mist: #b6c7c7;
    --ink: #595959;
    --note: #7a7a7a;
    --client: #16a6bd;
    --paper: #ffffff;
  }
  * { margin: 0; padding: 0; box-sizing: border-box; }
  html, body {
    width: 1200px; height: 901px; overflow: hidden;
    background: var(--paper);
    font-family: "Questrial", "Century Gothic", sans-serif;
  }
  .notes-page { position: relative; width: 1200px; height: 901px; }

  .slide {
    position: absolute; left: 82px; top: 28px;
    width: 1039px; height: 585px;
    background: var(--paper);
    border: 1.5px solid #1a1a1a;
    box-shadow: 3px 3px 5px rgba(0,0,0,0.35);
    overflow: hidden;
  }
  .band-column {
    position: absolute; top: 0; bottom: 0;
    display: flex; flex-direction: column; gap: 8px;
  }
  .band-column--left { left: 0; width: 75px; }
  .band-column--right { right: 0; width: 235px; }
  .band { flex: 1; }
  .band--navy { background: var(--navy); }
  .band--sage { background: var(--sage); }
  .band--sand { background: var(--sand); }
  .band--slate { background: var(--slate); }
  .band--mist { background: var(--mist); }

  .brand {
    position: absolute; left: 0; width: 880px; top: 38px;
    text-align: center; color: var(--navy);
  }
  .brand__disc {
    display: block; margin: 0 auto 10px;
    width: 86px; height: 86px; border-radius: 50%;
    background: var(--sage);
  }
  .brand__name {
    font-size: 44px; letter-spacing: 16px; line-height: 1;
    padding-left: 16px;
  }
  .brand__sub {
    font-size: 14px; letter-spacing: 6px; margin-top: 6px;
    padding-left: 6px;
  }

  .title {
    position: absolute; left: 0; width: 880px; top: 240px;
    text-align: center; color: var(--ink);
    font-size: 30px; font-weight: 400;
  }
  .presenter {
    position: absolute; left: 0; width: 880px; top: 302px;
    text-align: center; color: var(--ink); font-size: 21px;
  }
  .divider {
    position: absolute; left: 222px; width: 436px; top: 350px;
    height: 1.5px; background: var(--mist);
  }
  .client {
    position: absolute; left: 0; width: 880px; top: 425px;
    display: flex; justify-content: center; align-items: center; gap: 12px;
    color: var(--client); font-size: 46px;
  }
  .client__dot {
    width: 22px; height: 22px; border-radius: 50%; background: var(--client);
  }

  .notes {
    position: absolute; left: 82px; top: 675px; width: 1040px;
    color: var(--note); font-size: 18px; line-height: 24.5px;
  }
  .notes__lead { font-weight: 700; font-size: 16px; color: var(--ink); margin-bottom: 10px; }
  .page-number {
    position: absolute; right: 13px; top: 871px;
    color: var(--note); font-size: 14px;
  }
</style>
</head>
<body>
<main class="notes-page">
  <section class="slide">
    <div class="band-column band-column--left">
      <div class="band band--navy"></div>
      <div class="band band--sage"></div>
      <div class="band band--sand"></div>
      <div class="band band--slate"></div>
      <div class="band band--mist"></div>
    </div>
    <div class="band-column band-column--right">
      <div class="band band--navy"></div>
      <div class="band band--sage"></div>
      <div class="band band--sand"></div>
      <div class="band band--slate"></div>
      <div class="band band--mist"></div>
    </div>

    <div class="brand">
      <span class="brand__disc"></span>
      <div class="brand__name">DUNWICK</div>
      <div class="brand__sub">CONSULTING</div>
    </div>

    <h1 class="title">Management Consulting</h1>
    <p class="presenter">Leo Harwick</p>
    <div class="divider"></div>

    <div class="client">
      <span class="client__dot"></span>
      <span class="client__name">kova</span>
    </div>
  </section>

  <section class="notes">
    <p class="notes__lead">This is an image of the notes page in ppt.</p>
    <p>Here you can add important information if you are sending your presentation without a presenter.</p>
    <p>This is the Title page, room has been left for a second logo.</p>
    <p>The design is clean and simple reflecting the Dunwick logo style and colour scheme.</p>
  </section>

  <span class="page-number">1</span>
</main>
</body>
</html>
```